Roll Up Banner for Lifestyle / medical company

I need a roll-up banner for a congress highlighting our lifestyle company that aids people with diabetes type 2 through diet and exercise. The banner should capture our unique approach and appeal to medical professionals.

120x200 cm

Scope of work
- Design a roll-up banner for a congress.
- Include the programme name: Ons Suikerpad Route Schema.
- Add the catchphrase: Het individuele leefstijlprogramma voor 50-plussers met diabetes type 2.
- Feature the 4 pillars: Digitaal en persoonlijk, Duurzame begeleiding, Bewezen resultaten, Aanvulling ketenzorg.

References
- See our style at voedwijzerkracht.nl and in the files attached

Additional information
The banner should appeal to medical professionals attending the congress.

Company details
- Company website: voedwijzerkracht.nl
- We are a lifestyle company dedicated to helping people manage diabetes type 2 through tailored diet and exercise programs. Our target audience for this banner is medical professionals.

We can provide photo's of older individuals in our style. Contact us at info@voedwijzerkracht.nl for these pictures.

```html
<!DOCTYPE html>
<html lang="nl">
<head>
<meta charset="utf-8">
<title>Ons Suikerpad Route Schema – roll-up banner</title>
<link rel="stylesheet" href="https://fonts.googleapis.com/css2?family=Poppins:wght@300;400;700;800&display=swap">
<style>
  :root {
    --bg-top: #e3ecdd;
    --bg-bottom: #d4ded1;
    --brand-dark: #27604f;
    --teal: #1fa39a;
    --ink: #474747;
    --band: #0e4a41;
    --band-text: #e2eadf;
    --swoosh: #e7e9e7;
    --photo-light: #b49a83;
    --photo-dark: #6f5443;
  }
  * { margin: 0; padding: 0; box-sizing: border-box; }
  html, body { width: 768px; height: 1200px; overflow: hidden; }
  body { font-family: "Poppins", sans-serif; background: var(--bg-bottom); }

  .banner {
    position: relative;
    width: 768px;
    height: 1200px;
    overflow: hidden;
    background: linear-gradient(180deg, var(--bg-top) 0%, var(--bg-bottom) 100%);
  }

  .photo-area {
    position: absolute;
    left: 520px;
    top: 280px;
    width: 248px;
    height: 840px;
    border-top-left-radius: 24px;
    background: linear-gradient(170deg, var(--photo-light) 0%, #8d6c56 55%, var(--photo-dark) 100%);
  }

  .banner-base { position: absolute; inset: 0; width: 768px; height: 1200px; }

  .brand-name {
    position: absolute;
    left: 48px;
    top: 40px;
    font-weight: 800;
    font-size: 70px;
    line-height: 63px;
    letter-spacing: -3px;
    color: var(--brand-dark);
  }

  .programme-title {
    position: absolute;
    left: 48px;
    top: 306px;
    font-weight: 700;
    font-size: 62px;
    line-height: 70px;
    letter-spacing: -1px;
    color: var(--teal);
  }

  .tagline {
    position: absolute;
    left: 50px;
    top: 566px;
    width: 380px;
    font-weight: 400;
    font-size: 24px;
    line-height: 35px;
    color: var(--ink);
  }

  .pillars {
    position: absolute;
    left: 50px;
    top: 770px;
    list-style: none;
  }
  .pillar {
    display: flex;
    align-items: center;
    height: 48px;
    margin-bottom: 20px;
  }
  .pillar-icon { width: 44px; height: 44px; flex: none; margin-right: 32px; }
  .pillar-label {
    font-weight: 400;
    font-size: 18.5px;
    line-height: 23px;
    color: var(--ink);
  }

  .website {
    position: absolute;
    left: 0;
    width: 768px;
    top: 1118px;
    text-align: center;
    font-weight: 300;
    font-size: 38px;
    letter-spacing: 0.3px;
    color: var(--band-text);
  }
</style>
</head>
<body>
<main class="banner">
  <div class="photo-area" role="img" aria-label="Foto: oudere man in bruine trui met een mok, kijkt naar zijn telefoon"></div>

  <svg class="banner-base" viewBox="258 342 1025 1678" preserveAspectRatio="none" aria-hidden="true">
    <path class="bottom-swoosh" fill="var(--swoosh)" d="M258 1795 Q520 1880 940 1822 Q620 1890 258 1848 Z"/>
    <path class="bottom-band" fill="var(--band)" d="M258 1845 Q620 1905 950 1818 Q1160 1760 1283 1640 L1283 2020 L258 2020 Z"/>
  </svg>

  <div class="brand-name">voed<br>wijzer<br>kracht</div>

  <h1 class="programme-title">Ons<br>Suikerpad<br>Route Schema</h1>

  <p class="tagline">Het individuele<br>leefstijlprogramma<br>voor 50-plussers met<br>diabetes type 2.</p>

  <ul class="pillars">
    <li class="pillar">
      <svg class="pillar-icon" viewBox="0 0 44 44" fill="var(--teal)" stroke="var(--teal)" stroke-width="2">
        <circle cx="6" cy="10" r="3" stroke="none"/><circle cx="38" cy="10" r="3" stroke="none"/>
        <circle cx="6" cy="24" r="3" stroke="none"/><circle cx="38" cy="24" r="3" stroke="none"/>
        <circle cx="22" cy="4" r="3" stroke="none"/>
        <path d="M9 10 H16 M28 10 H35 M9 24 H16 M28 24 H35 M22 7 V12" fill="none"/>
        <rect x="15" y="12" width="14" height="12" rx="2" fill="none"/>
        <path d="M19 22 V36 Q19 42 26 42 H30 Q34 42 34 36 V29 Q34 27 31 27 H25 V20 Q25 17 22 17 Q19 17 19 20 Z" stroke="none"/>
      </svg>
      <span class="pillar-label">Digitaal<br>en persoonlijk</span>
    </li>
    <li class="pillar">
      <svg class="pillar-icon" viewBox="0 0 44 44" fill="var(--teal)">
        <rect x="1" y="24" width="7" height="14" rx="1"/>
        <path d="M10 26 H20 Q24 26 24 29 H16 V31 H26 L38 24 Q42 23 41 27 L28 38 Q26 40 22 40 H10 Z"/>
        <rect x="21" y="12" width="3" height="12"/>
        <path d="M22 14 Q12 16 10 6 Q20 4 22 14 Z"/>
        <path d="M23 12 Q26 2 38 2 Q36 12 23 12 Z"/>
      </svg>
      <span class="pillar-label">Duurzame<br>begeleiding</span>
    </li>
    <li class="pillar">
      <svg class="pillar-icon" viewBox="0 0 44 44">
        <circle cx="22" cy="22" r="14" fill="var(--teal)"/>
        <circle cx="22" cy="22" r="9" fill="#dfe8da"/>
        <path d="M17 22 L21 26 L28 18" fill="none" stroke="var(--teal)" stroke-width="3" stroke-linecap="round" stroke-linejoin="round"/>
        <g stroke="var(--teal)" stroke-width="2" stroke-linecap="round">
          <path d="M22 1 V4 M22 40 V43 M1 22 H4 M40 22 H43 M7 7 L9 9 M35 35 L37 37 M37 7 L35 9 M7 37 L9 35"/>
        </g>
      </svg>
      <span class="pillar-label">Bewezen<br>resultaten</span>
    </li>
    <li class="pillar">
      <svg class="pillar-icon" viewBox="0 0 44 44" fill="var(--teal)">
        <rect x="15" y="1" width="14" height="6" rx="1"/>
        <path d="M16 8 H28 V12 Q34 14 34 20 V41 Q34 43 32 43 H12 Q10 43 10 41 V20 Q10 14 16 12 Z"/>
        <rect x="13" y="25" width="18" height="11" fill="#dfe8da"/>
        <path d="M22 34 Q16 32 17 27 Q21 28 22 34 Q23 28 27 27 Q28 32 22 34 Z"/>
      </svg>
      <span class="pillar-label">Aanvulling<br>ketenzorg</span>
    </li>
  </ul>

  <p class="website">voedwijzerkracht.nl</p>
</main>
</body>
</html>
```